Major Australian Food and Wine Event Web Design Project

The project will consist of 3 designs
The homepage
A city hub page
A general content page

The main audience who will visit the website will be (in Order of importance:

1) Visitors
- Mainly women 24 – 54 years (they are the main ticket buyers)
- In a relationship – so will go to the show with their partner
- In a good paying job or home maker – and who have disposable income to spend $30 a ticker
- Enjoy food, wine and going out
- Looking for a fun day out – although an event that is about food and wine – it is an event that most people will go to and have a fun day out – not too pretentious

A smaller proportion of the audience will be:
2) Exhibitors & sponsors ( both prospective and existing)
3) Media

Objectives:

- Functionality on home page and sub pages needs to be updated, clear, easy to navigate and inject a sense of ‘fun’ – need to make it look more professional
- Need to incorporate the many things that need to be on the home page and sub pages in a visually appealing manner
- Ensure the ‘Cons’ above are considered and reflected in functionality and design
- To not be too focus on the colours (these can be changed) – but focus on the functionality and overall design opportunities.

Approach:

Keywords to describe the Bright Plate & Vine Fair:
Fun day out, discover, learn, indulge, entertaining

Other website examples:

Some great consumers event websites from the UK really make our website look basic and juvenile – and below are some examples of the presentation of how we would like our website to look like:

http://www.morselfairs-example.com/london/ This website is clean, includes good social media integration and exudes a sense of fun. Their content pages, such as the features landing page also presents options in a clear and visually appealing way with a series of boxes including image and text http://www.morselfairs-example.com/london/content/343/Features

http://www.homecraftexpo-example.com/ - this is also a great website – and it incorporates all the elements we would be looking for on our homepage – but the background/skin also includes a sense of fun and cheekiness. Subpages also are consistent.

Features

• Its a fun day that offers great value for money
• Caters to all visitors, regardless of different levels of knowledge or interest in food, wine and cooking.
• Sample great quality food and wine products from hundreds of reputable exhibitors
• Learn more through many of the shows feature activities (Celeb Theatre, Wine Theatre, Cooking & Cheese Classes)

Functionality & Structure:

In a user friendly, easy to view way, we need to incorporate the following functionality elements on home page:
- main header (that will incorporate our current creative) with a ‘fun’ skin
- navigation tabs/references (hone, location, tickets, blog, sign up, exhibitors)
- navigation/content banner (rotating)
- Area for small intro about the show
- News and highlight section
- New exhibitors section
- Obvious Ticket call to action
- Obvious sign up call to action
- Social media buttons or links ( really like the moving gifs on the Homecraftexpo-example.com site
- area for advertising (MREC size) to sell to exhibitors/sponsors
- Show dates for all 5 shows (maybe in main header)

Subpage layout is also important and needs to reflect the homepage – so would also like to see examples of how this would look and tie in with navigation – we generally have a lot of content on these pages, so clear navigation would be useful. – see below for further details of functionality for city Hubs

‘CITY HUB’ BRIEF
When navigating to each location the user will be taken to a ‘CITY HUB’ which should replicate design and content elements of a main HOME page, as well as reflect more specific information for each Show. Elements which must appear on this page are:
• FEATURES – which may be displayed in categories (in boxes, see appendix 1.0) which will link through to relevant content pages. Or in one box which will link through to a features page with all presented in boxes
• CHEFS – may be displayed as a separate icon box which will link to chefs page with bios, Celeb Theatre timetable etc.
• TICKETS – either a button or clear callout to purchase tickets
• PLAN YOUR DAY – may be displayed in a separate content box which will then link through to getting there, sample itineraries and downloadable pocket show guide for visitors to print before coming to the Show.
• WHO’S EXHIBITING – to link back to city specific exhibitor lists

Our current website is out of date and has the following inadequacies (www.brightplatefair-example.com.au) -

The homepage
A city hub page
A general content page

1) Visitors

3) Media

Objectives:

Approach:

To be perceived as a fun, entertaining event with something for everyone - website creative and navigation must reflect this.

Other website examples:

Features

- New exhibitors section

‘CITY HUB’ BRIEF

- Dated design/layout
- Homepage too text heavy
- No content boxes that can be used for different features/areas (eg. News, Exhibitors etc)
- Uninspiring colours and skin(eg. grey background), does not reflect ‘a fun day out’
- Limited presence of social media platforms and lacks ‘community’
- No continuity in sub pages
- main banner too big – takes up too much space on homepage

Requirements
Must have
• As per above brief.

In addition:
Floating social media buttons on side
Wrap around image
Drop down menu (specifically for the location nav item)

```html
<!DOCTYPE html>
<html lang="en">
<head>
<meta charset="utf-8">
<title>Bright Plate &amp; Vine Fair 2012</title>
<link href="https://fonts.googleapis.com/css2?family=Roboto:wght@400;500&family=Arimo:wght@400;700&family=Alfa+Slab+One&display=swap" rel="stylesheet">
<style>
:root{
  --navy:#1f0f96;
  --navy-dark:#170b78;
  --orange:#ea5a1b;
  --orange-light:#f47a3a;
  --text:#222;
  --muted:#9a9a9a;
  --sidebar:#dfe3f2;
  --footer:#b9c6e6;
  --wood:#9c7b5c;
  --ad-text:#f6ec2a;
}
*{box-sizing:border-box;margin:0;padding:0}
html,body{width:1000px;height:1200px;overflow:hidden}
body{position:relative;font-family:"Arimo",Arial,sans-serif;color:var(--text);
  background:linear-gradient(90deg,#8a6a4c 0%,#b0906f 20%,#9c7b5c 45%,#b89878 70%,#8c6c4e 100%)}
.abs{position:absolute}
.wood-backdrop{left:0;top:0;width:1000px;height:1200px}
.leaf-left{left:0;top:200px;width:120px;height:700px;background:linear-gradient(180deg,rgba(126,160,60,.55),rgba(96,130,40,.35));border-radius:0 60% 60% 0}
.leaf-right{left:850px;top:200px;width:150px;height:750px;background:linear-gradient(180deg,rgba(140,170,60,.5),rgba(100,130,40,.35));border-radius:60% 0 0 60%}
.header-scene{left:300px;top:0;width:548px;height:207px;background:linear-gradient(160deg,#d94a4a 0%,#f0d8d8 45%,#c83a3a 100%)}
.logo-banner{left:118px;top:0;width:193px;height:191px;background:#fff;clip-path:polygon(0 0,100% 0,100% 90%,50% 100%,0 90%);
  display:flex;align-items:center;justify-content:center;text-align:center;padding:0 14px}
.logo-name{font-family:"Roboto",sans-serif;font-weight:400;font-size:26px;line-height:1.1;color:#222}
.dates-ribbon{left:444px;top:25px;width:270px;height:98px;background:linear-gradient(90deg,var(--orange),var(--orange-light));
  transform:rotate(2deg);padding:12px 0 0 38px;font-family:"Roboto",sans-serif;font-size:13px;color:#fde5d6;line-height:18px}
.dates-ribbon span{display:inline-block;width:84px}
.nav{left:116px;top:207px;width:515px;height:29px;background:var(--navy);display:flex}
.nav a{font-family:"Roboto",sans-serif;font-weight:500;font-size:13px;letter-spacing:.5px;color:#fff;text-decoration:none;
  padding:0 17px;line-height:29px;border-right:1px solid #4a3db3}
.sidebar{left:635px;top:207px;width:213px;height:768px;background:var(--sidebar)}
.main{left:116px;top:236px;width:515px;height:739px;background:#fff}
.hero{left:116px;top:236px;width:515px;height:246px;background:linear-gradient(120deg,#6c6c6c,#cfcfcf 50%,#8a7d78)}
.slider-dots{left:488px;top:461px;display:flex;gap:1px}
.slider-dots i{display:block;width:26px;height:16px;background:rgba(255,255,255,.45)}
.slider-dots i.on{background:#5b4bc0}
h2.section{font-family:"Roboto",sans-serif;font-weight:400;font-size:12px;color:var(--navy);position:absolute}
.rule{position:absolute;height:2px;background:var(--navy)}
.body-copy{font-size:9.5px;line-height:12.5px;color:var(--text)}
.cta{background:var(--orange);color:#fff;font-family:"Roboto",sans-serif;font-size:12px;letter-spacing:.4px;
  clip-path:polygon(0 0,96% 0,100% 50%,96% 100%,0 100%,3% 50%);display:flex;align-items:center;justify-content:center}
.tabs{left:129px;top:629px;display:flex;font-family:"Roboto",sans-serif;font-size:12px}
.tabs span{padding:0 7px;line-height:22px}
.tabs .active{background:var(--navy);color:#fff}
.tabs .idle{background:#e2e2e2;color:#666}
.news-title{font-size:10px;font-weight:700;color:#333;text-decoration:underline;position:absolute}
.news-text{position:absolute;width:235px}
.news-text .date{color:var(--muted)}
.tweet{position:absolute;width:235px}
.tweet b{color:var(--navy)}
.tweet a{color:var(--navy);text-decoration:none}
.tweet .ago{color:var(--muted);display:block;margin-top:4px}
.ex-title{position:absolute;font-size:10px;font-weight:700;color:#333;text-decoration:underline}
.ex-text{position:absolute;width:145px}
.ex-img{position:absolute;left:541px;width:77px}
.side-title{font-family:"Roboto",sans-serif;font-size:12px;color:var(--navy);position:absolute}
.email{left:644px;top:235px;width:147px;height:22px;background:#fff;border:1px solid #ccd;font-size:10px;color:#999;padding:5px 9px}
.signup{left:793px;top:235px;width:47px;height:22px;background:var(--navy);color:#fff;font-size:10.5px;text-align:center;line-height:22px}
.book-box{left:644px;top:280px;width:196px;height:71px;background:linear-gradient(180deg,#9a9a9a,#5a5a5a)}
.book-btn{left:680px;top:300px;width:150px;height:25px;font-size:12px}
.photos-box{left:644px;top:361px;width:196px;height:78px;background:#c9ccd6}
.thumbs{left:656px;top:386px;width:164px;height:42px;background:linear-gradient(90deg,#b23,#daa 40%,#c97 70%,#edc);border:2px solid #fff}
.ad{position:absolute;left:644px;width:196px;background:#000;display:flex;align-items:center;justify-content:center;text-align:center;
  font-family:"Alfa Slab One",serif;font-size:15px;line-height:16px;color:var(--ad-text)}
.social{left:848px;top:235px;width:36px;height:174px;background:#fff;display:flex;flex-direction:column;align-items:center;gap:14px;padding-top:9px}
.social i{display:block;width:24px;height:24px;border-radius:3px}
.footer{left:116px;top:975px;width:732px;height:170px;background:linear-gradient(180deg,#a8b7de,#d2dbf0)}
.quicklinks{left:134px;top:1023px;display:grid;grid-template-columns:117px 110px;row-gap:3.4px;font-family:"Roboto",sans-serif;font-size:11px;color:var(--navy)}
.dates-box{left:375px;top:976px;width:245px;height:154px;background:var(--orange);color:#fff;font-family:"Roboto",sans-serif}
.dates-box h3{font-weight:500;font-size:12px;padding:15px 0 0 13px;height:33px}
.dates-box .line{height:2px;background:#fff;opacity:.8}
.dates-box table{margin:10px 0 0 13px;font-size:12.5px;border-spacing:0}
.dates-box td{height:17.7px;padding-right:14px}
.footer-logo{left:721px;top:977px;width:118px;height:114px;background:#fff;clip-path:polygon(0 0,100% 0,100% 88%,50% 100%,0 88%);
  display:flex;align-items:center;justify-content:center;text-align:center;padding:0 8px;font-family:"Roboto",sans-serif;font-size:15px;line-height:1.15;color:#222}
.copyright{left:131px;top:1152px;font-size:9.5px;font-weight:700;color:#fff}
</style>
</head>
<body>
<div class="abs wood-backdrop" role="img" aria-label="Weathered wooden plank backdrop"></div>
<div class="abs leaf-left" role="img" aria-label="Vine leaves, chillies and herbs wrapping the left edge"></div>
<div class="abs leaf-right" role="img" aria-label="Vine leaves and dark grapes wrapping the right edge"></div>

<header>
  <div class="abs header-scene" role="img" aria-label="Checked tablecloth with cheese, avocado, grapes, a hen and a crayfish"></div>
  <div class="abs logo-banner"><span class="logo-name">Bright Plate &amp; Vine Fair</span></div>
  <div class="abs dates-ribbon">
    <div><span>SYDNEY</span>22nd–24th June</div>
    <div><span>MELBOURNE</span>22nd–24th July</div>
    <div><span>PERTH</span>22nd–24th August</div>
    <div><span>BRISBANE</span>22nd–24th September</div>
  </div>
</header>

<aside class="abs sidebar"></aside>
<main class="abs main"></main>

<nav class="abs nav">
  <a>HOME</a><a>LOCATION</a><a>TICKETS</a><a>BLOG</a><a>SIGN UP</a><a style="border-right:0">EXHIBITORS</a>
</nav>

<div class="abs hero" role="img" aria-label="Chef drizzling sauce over plated sliced meat"></div>
<div class="abs slider-dots"><i class="on"></i><i></i><i></i><i></i><i></i></div>

<h2 class="section" style="left:129px;top:493px">The Bright Plate &amp; Vine Fair 2012</h2>
<div class="rule" style="left:129px;top:510px;width:491px"></div>
<p class="abs body-copy" style="left:130px;top:519px;width:480px">Lorem Ipsum is simply dummy text of the printing and typesetting industry. Lorem Ipsum has been the industry's standard dummy text ever since the 1500s, when an unknown printer took a galley of type and scrambled it to make a type specimen book.</p>
<svg class="abs" style="left:132px;top:559px" width="42" height="40" viewBox="0 0 42 40" aria-label="Calendar" role="img">
  <rect x="2" y="4" width="38" height="34" rx="3" fill="#f4f4f4" stroke="#aaa"/>
  <rect x="2" y="4" width="38" height="8" rx="3" fill="#bbb"/>
  <g fill="#999"><rect x="7" y="16" width="5" height="4"/><rect x="15" y="16" width="5" height="4"/><rect x="23" y="16" width="5" height="4"/><rect x="31" y="16" width="5" height="4"/>
  <rect x="7" y="23" width="5" height="4"/><rect x="15" y="23" width="5" height="4"/><rect x="23" y="23" width="5" height="4"/><rect x="31" y="23" width="5" height="4"/>
  <rect x="7" y="30" width="5" height="4"/><rect x="15" y="30" width="5" height="4"/></g>
</svg>
<p class="abs body-copy" style="left:181px;top:567px;width:180px">Sydney show starts in 14 weeks,<br>early bird tickets on sale now.</p>
<div class="abs cta" style="left:375px;top:567px;width:214px;height:24px">GET EARLYBIRD TICKETS NOW</div>

<div class="abs tabs"><span class="active">Latest News</span><span class="idle">Highlights</span></div>
<div class="rule" style="left:129px;top:651px;width:235px"></div>
<div class="news-title" style="left:129px;top:663px">Best in Show Wine Awards</div>
<p class="news-text body-copy" style="left:129px;top:679px"><span class="date">10 Jan 2012</span> There are many variations of passages of Lorem Ipsum available, but the majority have suffered alteration in some form.</p>
<div class="news-title" style="left:129px;top:736px">New Chef announcements</div>
<p class="news-text body-copy" style="left:129px;top:752px"><span class="date">12 Jan 2012</span> There are many variations of passages of Lorem Ipsum available, but the majority have suffered alteration in some form.</p>

<div class="abs" style="left:129px;top:808px;width:235px;height:1px;background:#ccc"></div>
<h2 class="section" style="left:129px;top:815px">Chirpline</h2>
<span class="abs" style="left:275px;top:815px;font-family:Roboto,sans-serif;font-size:12px;color:#444">#BrightPlate2012</span>
<div class="rule" style="left:129px;top:832px;width:235px"></div>
<p class="tweet body-copy" style="left:129px;top:845px"><b>brightplate2012:</b> Cooking tonight? Make double and put next week's dinner on ice: <a>lnk.example/A0eEuJ</a><span class="ago">7 hours ago</span></p>
<p class="tweet body-copy" style="left:129px;top:905px"><b>brightplate2012:</b> Fancy yourself as the next big food writer? Here's our guide to writing a recipe. Let us know your hints and tips: <a>lnk.example/xHmS4J</a><span class="ago">11 hours ago.</span></p>

<div class="abs" style="left:379px;top:627px;width:241px;height:2px;background:#ddd"></div>
<h2 class="section" style="left:379px;top:635px">New Exhibitors in 2012</h2>
<div class="rule" style="left:379px;top:652px;width:239px"></div>
<div class="ex-title" style="left:379px;top:663px">Highmeadow Berry Farm</div>
<p class="ex-text body-copy" style="left:379px;top:679px">The standard chunk of Lorem Ipsum used since the 1500s is reproduced below for those interested.</p>
<div class="ex-img" style="top:661px;height:75px;background:linear-gradient(135deg,#f3e8dc,#c2434a 60%,#6a8a3a)" role="img" aria-label="Berry tart with cream"></div>
<div class="ex-title" style="left:379px;top:745px">Ridgefold Wines</div>
<p class="ex-text body-copy" style="left:379px;top:761px">The standard chunk of Lorem Ipsum used since the 1500s is reproduced below for those interested.</p>
<div class="ex-img" style="top:747px;height:77px;background:linear-gradient(160deg,#b8b0ac,#6e5a58 60%,#3a3232)" role="img" aria-label="Stacked wooden wine crates"></div>
<div class="ex-title" style="left:379px;top:834px">Southbay Avocado Oil</div>
<p class="ex-text body-copy" style="left:379px;top:850px">The standard chunk of Lorem Ipsum used since the 1500s is reproduced below for those interested.</p>
<div class="ex-img" style="top:830px;height:80px;background:linear-gradient(150deg,#fff 30%,#e8d070 60%,#6a9a30)" role="img" aria-label="Bottle of oil beside a halved avocado"></div>

<h2 class="side-title" style="left:644px;top:214px">Get newsletter updates</h2>
<div class="abs email">Your email</div>
<div class="abs signup">Sign up</div>
<div class="abs book-box" role="img" aria-label="Dusky road scene behind ticket banner"></div>
<div class="abs cta book-btn">BOOK TICKETS NOW</div>
<div class="abs photos-box"></div>
<h2 class="side-title" style="left:656px;top:367px">Check out the Show in photos</h2>
<div class="abs thumbs" role="img" aria-label="Fanned show photos of stalls and visitors"></div>
<div class="ad" style="top:445px;height:223px">Advertising<br>Placer</div>
<div class="ad" style="top:675px;height:132px">Advertising<br>Placer</div>
<div class="ad" style="top:815px;height:135px">Advertising<br>Placer</div>

<div class="abs social" aria-label="Social links">
  <i style="background:#3b5ba0" aria-label="Social link one"></i>
  <i style="background:#3fa0da" aria-label="Social link two"></i>
  <i style="background:#d8312b" aria-label="Social link three"></i>
  <i style="background:#e6e6e6" aria-label="Social link four"></i>
</div>

<footer>
  <div class="abs footer"></div>
  <h2 class="section" style="left:129px;top:989px">Quicklinks</h2>
  <div class="rule" style="left:129px;top:1008px;width:235px"></div>
  <div class="abs quicklinks">
    <span>HOME</span><span>ABOUT US</span>
    <span>LOCATION</span><span>CONTACT US</span>
    <span>TICKETS</span><span>FEEDBACK</span>
    <span>BLOG</span><span>TERMS OF USE</span>
    <span>SIGN UP</span><span>PRIVACY POLICY</span>
    <span>EXHIBITORS</span><span></span>
  </div>
  <div class="abs dates-box">
    <h3>Bright Plate &amp; Vine Fair 2012 Dates</h3>
    <div class="line"></div>
    <table>
      <tr><td>SYDNEY</td><td>22nd–24th June</td></tr>
      <tr><td>MELBOURNE</td><td>22nd–24th July</td></tr>
      <tr><td>PERTH</td><td>22nd–24th August</td></tr>
      <tr><td>BRISBANE</td><td>22nd–24th September</td></tr>
    </table>
  </div>
  <div class="abs footer-logo">Bright Plate &amp; Vine Fair</div>
  <p class="abs copyright">Copyright © 2012 Bright Plate &amp; Vine Fair. All Rights Reserved.</p>
</footer>
</body>
</html>
```